TalkBridge - Language Coaching Services

Sleek, innovative, trendy design for Language Coaching business.

TalkBridge is a new UK based company that provides Language Coaching services. We offer highly personalized on-line and face to face language courses. We also impart learning techniques workshops based on the latest neuroscience research for second-language acquisition.

Target Market(s)

Industry/Entity Type

Consulting

Contact Information for Business Card

TalkBridge
ElenaVT@talkbridge-demo.co.uk
TalkBridge-demo.co.uk
London, UK

Font styles to use
Sans Serif

```html
<!DOCTYPE html>
<html lang="en">
<head>
<meta charset="utf-8">
<title>TalkBridge – Business Card</title>
<link rel="stylesheet" href="https://fonts.googleapis.com/css2?family=Roboto:wght@400;500;700&display=swap">
<style>
  :root {
    --stage: #e6e8eb;
    --card-dark: #1c1d1f;
    --card-light: #ffffff;
    --brand-blue: #0f7fc0;
    --brand-blue-deep: #0b5f97;
    --brand-blue-light: #26a3e0;
    --text-grey: #7a7d80;
    --text-dark: #3c3f42;
    --text-on-dark: #d9dbdd;
    --tint: #eef5fa;
  }
  * { box-sizing: border-box; margin: 0; padding: 0; }
  html, body { width: 1200px; height: 960px; overflow: hidden; }
  body {
    background: var(--stage);
    font-family: "Roboto", Arial, sans-serif;
    position: relative;
  }
  .card {
    position: absolute;
    width: 630px;
    height: 360px;
    border-radius: 4px;
    overflow: hidden;
    box-shadow: 0 10px 30px rgba(0,0,0,.18);
  }

  /* Back of card */
  .card--back {
    left: 90px; top: 90px;
    background: var(--card-dark);
  }
  .back-mark {
    position: absolute;
    left: 50%; top: 46%;
    transform: translate(-50%, -50%);
    display: flex; align-items: center; gap: 16px;
  }
  .back-mark__dot {
    width: 40px; height: 40px; border-radius: 50%;
    border: 6px solid var(--brand-blue);
  }
  .back-mark__name {
    font-weight: 700; font-size: 44px; color: var(--brand-blue);
    letter-spacing: .5px;
  }
  .back-web {
    position: absolute;
    left: 0; right: 0; bottom: 74px;
    text-align: center;
    font-size: 15px; color: var(--text-on-dark); letter-spacing: 2px;
  }

  /* Front of card */
  .card--front {
    left: 480px; top: 470px;
    background: var(--card-light);
  }
  .front-art { position: absolute; inset: 0; }
  .front-brand {
    position: absolute; right: 60px; top: 60px;
    display: flex; align-items: center; gap: 12px;
  }
  .front-brand__dot {
    width: 30px; height: 30px; border-radius: 50%;
    border: 4px solid var(--brand-blue);
  }
  .front-brand__name {
    font-weight: 700; font-size: 38px; color: var(--brand-blue);
  }
  .person { position: absolute; left: 40px; top: 198px; }
  .person__name {
    font-weight: 700; font-size: 23px; line-height: 28px;
    color: var(--brand-blue-deep); letter-spacing: .3px;
  }
  .person__title {
    font-size: 14px; line-height: 18px; color: var(--text-grey); margin-top: 1px;
  }
  .contact { position: absolute; left: 40px; top: 258px; list-style: none; }
  .contact li {
    display: flex; align-items: center; gap: 10px;
    font-size: 15px; color: var(--text-dark); line-height: 22px;
  }
  .contact svg { width: 14px; height: 14px; flex: none; }
  .front-web {
    position: absolute; right: 26px; bottom: 28px;
    font-size: 14px; color: #fff; letter-spacing: .3px;
  }
</style>
</head>
<body>

<section class="card card--back" aria-label="Card back">
  <div class="back-mark">
    <span class="back-mark__dot"></span>
    <span class="back-mark__name">TalkBridge</span>
  </div>
  <p class="back-web">talkbridge-demo.co.uk</p>
</section>

<section class="card card--front" aria-label="Card front">
  <svg class="front-art" viewBox="0 0 630 360" aria-hidden="true">
    <circle cx="150" cy="150" r="120" fill="var(--tint)"/>
    <line x1="40" y1="190" x2="580" y2="170" stroke="var(--brand-blue)" stroke-width="2"/>
    <polygon points="592,169.6 578,164 579,176" fill="var(--brand-blue)"/>
    <line x1="40" y1="250" x2="360" y2="250" stroke="var(--brand-blue)" stroke-width="1"/>
    <path d="M0 326 L390 326 Q410 326 416 306 Q422 290 440 290 L630 290 L630 360 L0 360 Z" fill="var(--brand-blue)"/>
    <path d="M0 312 L380 312 Q400 312 406 298 Q412 284 430 284 L630 284" fill="none" stroke="var(--brand-blue-light)" stroke-width="3"/>
    <rect x="0" y="338" width="630" height="4" fill="#fff" opacity=".6"/>
  </svg>

  <div class="front-brand">
    <span class="front-brand__dot"></span>
    <span class="front-brand__name">TalkBridge</span>
  </div>

  <div class="person">
    <h1 class="person__name">ELENAVT</h1>
    <p class="person__title">CEO/FOUNDER</p>
  </div>

  <ul class="contact">
    <li>
      <svg viewBox="0 0 14 14"><path d="M7 13.5 C4 9.5 2.5 7.3 2.5 5 A4.5 4.5 0 0 1 11.5 5 C11.5 7.3 10 9.5 7 13.5 Z" fill="var(--brand-blue)"/><circle cx="7" cy="5" r="1.6" fill="#fff"/></svg>
      London, UK
    </li>
    <li>
      <svg viewBox="0 0 14 14"><rect x="0.5" y="2.5" width="13" height="9" fill="var(--brand-blue)"/><path d="M0.5 2.5 L7 8 L13.5 2.5" fill="none" stroke="#fff" stroke-width="1.2"/></svg>
      ElenaVT@talkbridge-demo.co.uk
    </li>
  </ul>

  <p class="front-web">www.talkbridge-demo.co.uk</p>
</section>

</body>
</html>
```